Building Company Business Card Design

I am looking to get a business card designed for my Building Company. Please find the logo attached.

Industry/Entity Type

Business

Contact Information for Business Card

Mobile 0472 913 046
Email admin@tarrowconstructworks.com.au
Website www.tarrowconstructworks.com.au

Colors
0255a3

```html
<!DOCTYPE html>
<html lang="en">
<head>
<meta charset="utf-8">
<title>Tarrow Constructworks – Business Card</title>
<link href="https://fonts.googleapis.com/css2?family=Montserrat:wght@400;600&display=swap" rel="stylesheet">
<style>
  :root {
    --brand-blue: #0255a3;
    --backdrop: #c6c6c8;
    --card-white: #f4f4f4;
    --text-grey: #3a3a3a;
    --ghost: #e9eaee;
  }
  html, body {
    margin: 0;
    padding: 0;
    width: 1200px;
    height: 1200px;
    overflow: hidden;
    background: var(--backdrop);
    font-family: "Montserrat", Arial, sans-serif;
  }
  .stage {
    position: relative;
    width: 1200px;
    height: 1200px;
  }
  .card {
    position: absolute;
    left: 252px;
    width: 696px;
    height: 400px;
    box-sizing: border-box;
  }
  .card-front {
    top: 150px;
    background: #fff;
    padding: 11px;
  }
  .card-front .face {
    width: 100%;
    height: 100%;
    background: var(--brand-blue);
    display: flex;
    align-items: center;
    justify-content: center;
  }
  .brand-name {
    font-weight: 600;
    letter-spacing: 0.02em;
    text-transform: uppercase;
    margin: 0;
    white-space: nowrap;
    line-height: 1.2;
  }
  .card-front .brand-name {
    color: #fff;
    font-size: 26px;
    margin-top: 10px;
  }
  .card-back {
    top: 630px;
    background: var(--card-white);
    overflow: hidden;
  }
  .ghost-name {
    position: absolute;
    left: 22px;
    top: 114px;
    color: var(--ghost);
    font-size: 40px;
  }
  .back-name {
    position: absolute;
    left: 22px;
    top: 250px;
    color: var(--brand-blue);
    font-size: 19px;
  }
  .contacts {
    position: absolute;
    right: 26px;
    top: 293px;
    margin: 0;
    padding: 0;
    list-style: none;
  }
  .contacts li {
    display: flex;
    align-items: center;
    justify-content: flex-end;
    height: 23px;
    font-size: 14px;
    color: var(--text-grey);
    letter-spacing: 0.03em;
  }
  .contacts svg {
    width: 15px;
    height: 15px;
    margin-left: 12px;
    flex: none;
  }
</style>
</head>
<body>
<main class="stage">
  <section class="card card-front" aria-label="Card front">
    <div class="face">
      <p class="brand-name">Tarrow Constructworks</p>
    </div>
  </section>

  <section class="card card-back" aria-label="Card back">
    <p class="brand-name ghost-name" aria-hidden="true">Tarrow Constructworks</p>
    <p class="brand-name back-name">Tarrow Constructworks</p>
    <ul class="contacts">
      <li>0472 913 046
        <svg viewBox="0 0 15 15" aria-hidden="true"><rect width="15" height="15" fill="var(--brand-blue)"/><rect x="5" y="3" width="5" height="9" rx="0.8" fill="none" stroke="#fff" stroke-width="1.1"/></svg>
      </li>
      <li>admin@tarrowconstructworks.com.au
        <svg viewBox="0 0 15 15" aria-hidden="true"><rect width="15" height="15" fill="var(--brand-blue)"/><rect x="3" y="4.5" width="9" height="6" fill="none" stroke="#fff" stroke-width="1"/><path d="M3 4.5 L7.5 8 L12 4.5" fill="none" stroke="#fff" stroke-width="1"/></svg>
      </li>
      <li>www.tarrowconstructworks.com.au
        <svg viewBox="0 0 15 15" aria-hidden="true"><rect width="15" height="15" fill="var(--brand-blue)"/><circle cx="7.5" cy="7.5" r="4" fill="none" stroke="#fff" stroke-width="1"/><path d="M3.5 7.5 H11.5 M7.5 3.5 C5.5 6 5.5 9 7.5 11.5 M7.5 3.5 C9.5 6 9.5 9 7.5 11.5" fill="none" stroke="#fff" stroke-width="0.8"/></svg>
      </li>
    </ul>
  </section>
</main>
</body>
</html>
```